Business Card Design for Animal Clinic

We are seeking a two sided business card design. The primary side should include our logo (provided in AI and EPS files) address, phone, website, and if possible "Follow Us" with icons for Facebook, Google+, and Twitter.

The back of the card needs to included space for appointment reminders.

Company Name:
Brackenfield Animal Clinic

Doctor Name:
To be provided to winner

Adress:
To be provided to winner

Phone:
to be provided to winner

Website:
www.brackenfieldanimalclinic.example

```html
<!DOCTYPE html>
<html lang="en">
<head>
<meta charset="utf-8">
<title>Brackenfield Animal Clinic – Business Card</title>
<link rel="stylesheet" href="https://fonts.googleapis.com/css2?family=Open+Sans:wght@400;700&display=swap">
<style>
  :root {
    --backdrop: #ece9e6;
    --card: #ffffff;
    --clinic-red: #b8323e;
    --deep-red: #9e2430;
    --soft-red: #c84a55;
    --tan: #d39a78;
    --ink: #333333;
    --line-red: #c23b47;
  }
  * { margin: 0; padding: 0; box-sizing: border-box; }
  html, body {
    width: 1200px; height: 800px; overflow: hidden;
    background: var(--backdrop);
    font-family: "Open Sans", Arial, sans-serif;
  }
  .canvas { position: relative; width: 1200px; height: 800px; }
  .card {
    position: absolute;
    background: var(--card);
    box-shadow: 0 6px 18px rgba(0,0,0,0.18);
    overflow: hidden;
  }

  /* Back side: appointment reminder */
  .card-back { left: 70px; top: 85px; width: 360px; height: 630px; }
  .appointment-line {
    position: absolute; top: 30px; width: 3px; height: 230px;
    background: var(--line-red);
  }
  .appointment-line.first { left: 40px; }
  .appointment-line.second { left: 90px; }
  .appointment-label {
    position: absolute; left: 120px; top: 28px;
    writing-mode: vertical-rl;
    color: var(--clinic-red);
    font-weight: 700; font-size: 17px; letter-spacing: 0.5px;
  }
  .back-feature {
    position: absolute; left: 0; bottom: 0; width: 100%; height: 340px;
    background: linear-gradient(160deg, var(--soft-red), var(--deep-red));
    border-top-right-radius: 180px;
  }

  /* Front side: contact details */
  .card-front { left: 500px; top: 220px; width: 630px; height: 360px; }
  .clinic-name {
    position: absolute; right: 40px; top: 34px;
    display: flex; align-items: center; gap: 12px;
    color: var(--clinic-red);
    font-size: 30px; font-weight: 400; letter-spacing: 1px;
    text-transform: uppercase;
  }
  .clinic-mark {
    width: 20px; height: 20px; border-radius: 50%;
    background: var(--clinic-red);
  }
  .contact {
    position: absolute; left: 250px; top: 120px;
    color: var(--ink); font-size: 16px; line-height: 1.45;
  }
  .doctor-name {
    color: var(--clinic-red); font-weight: 700; font-size: 22px;
    text-transform: uppercase; margin-bottom: 6px;
  }
  .follow { display: flex; align-items: center; gap: 8px; }
  .follow-mark { width: 14px; height: 14px; background: var(--clinic-red); }
  .front-band { position: absolute; left: 0; top: 0; }
  .band-url {
    fill: #ffffff; font-family: "Open Sans", Arial, sans-serif;
    font-size: 17px; letter-spacing: 1.5px;
  }
</style>
</head>
<body>
<main class="canvas">
  <section class="card card-back" aria-label="Card back">
    <div class="appointment-line first"></div>
    <div class="appointment-line second"></div>
    <p class="appointment-label">Next appointment:</p>
    <div class="back-feature" role="img" aria-label="Large red heart decoration with pet silhouettes"></div>
  </section>

  <section class="card card-front" aria-label="Card front">
    <svg class="front-band" width="630" height="360" viewBox="0 0 630 360">
      <path d="M0,150 Q300,190 470,360" fill="none" stroke="var(--tan)" stroke-width="10"/>
      <path id="band-edge" d="M0,160 Q300,200 465,360 L0,360 Z" fill="var(--clinic-red)"/>
      <path id="url-path" d="M20,200 Q280,232 420,360" fill="none"/>
      <text class="band-url"><textPath href="#url-path">www.brackenfieldanimalclinic.example</textPath></text>
    </svg>
    <div class="clinic-name">
      <span>Brackenfield Animal Clinic</span>
      <span class="clinic-mark"></span>
    </div>
    <div class="contact">
      <p class="doctor-name">Dana Whitlock</p>
      <p>555-010-4821</p>
      <p>danawhitlock@mail.example</p>
      <p class="follow">Follow us <span class="follow-mark"></span></p>
    </div>
  </section>
</main>
</body>
</html>
```